ORLUq Business card. A.I. company developing trading strategies.

My name is tommaso fabbri and I'm CEO and co-founder of ORLUQ Research, an AI company focusing on generating Ai-driven trading strategies.
This is our website: https://orluq-research.example/
Values of our company: tech & R&D driven (we're all very mathy/stats/data driven), sophisticated (we only look for sophisticated, high knowledge investors), reserved (we don't go around telling anyone what we do).
Our main product: KobraFNX. A trading strategy that delivered 70% in 2022 and 20% in 2023 so far.
Our main potential clients: HNW individuals, hedge funds, asset managers, tech entrepreneur.
Hedge funds, asset managers, High Net Worth individuals, Pension funds
The basic: name, job title, company name, address, mail, phone number

```html
<!DOCTYPE html>
<html lang="en">
<head>
<meta charset="utf-8">
<title>ORLUq Research – Business Card</title>
<link rel="stylesheet" href="https://fonts.googleapis.com/css2?family=Arimo:wght@400;700&display=swap">
<style>
  :root {
    --backdrop: #d8d3cb;
    --card-surface: #ecebe8;
    --ink-dark: #2a2a2c;
    --ink-body: #333335;
    --accent-red: #8c1c26;
    --rule: #4a4a4c;
    --band-dark: #1f1f21;
  }
  * { margin: 0; padding: 0; box-sizing: border-box; }
  html, body {
    width: 1200px;
    height: 969px;
    overflow: hidden;
    background: var(--backdrop);
    font-family: "Arimo", Arial, sans-serif;
  }
  .business-card {
    position: absolute;
    left: 100px;
    top: 198px;
    width: 1000px;
    height: 572px;
    background: var(--card-surface);
    border-radius: 4px;
    box-shadow: 0 10px 30px rgba(0,0,0,0.12);
    overflow: hidden;
  }
  .brand-name {
    position: absolute;
    right: 90px;
    top: 78px;
    font-size: 46px;
    font-weight: 400;
    letter-spacing: 3px;
    color: var(--ink-dark);
    line-height: 1;
  }
  .brand-sub {
    position: absolute;
    right: 90px;
    top: 134px;
    font-size: 17px;
    font-weight: 400;
    letter-spacing: 4px;
    color: var(--ink-dark);
    text-transform: uppercase;
  }
  .person-name {
    position: absolute;
    left: 87px;
    top: 318px;
    font-size: 30px;
    font-weight: 700;
    color: var(--ink-dark);
  }
  .person-title {
    position: absolute;
    left: 87px;
    top: 360px;
    font-size: 20px;
    color: var(--accent-red);
  }
  .divider {
    position: absolute;
    left: 87px;
    top: 395px;
    width: 833px;
    height: 2px;
    background: var(--rule);
  }
  .contact-left, .contact-right {
    position: absolute;
    top: 428px;
    font-size: 24px;
    line-height: 30px;
    color: var(--ink-body);
  }
  .contact-left { left: 87px; }
  .contact-right { right: 80px; text-align: right; }
  .contact-line { display: flex; align-items: center; justify-content: flex-end; gap: 10px; }
  .contact-icon { width: 20px; height: 20px; fill: var(--accent-red); }
  .band-dark {
    position: absolute;
    left: 0; bottom: 6px;
    width: 655px; height: 20px;
    background: var(--band-dark);
  }
  .band-red {
    position: absolute;
    left: 665px; bottom: 6px;
    right: 0; height: 20px;
    background: var(--accent-red);
  }
</style>
</head>
<body>
  <div class="business-card">
    <div class="brand-name">ORLUq</div>
    <div class="brand-sub">Research</div>

    <div class="person-name">Tommaso fabbri</div>
    <div class="person-title">CEO &amp; co-founder</div>
    <div class="divider"></div>

    <div class="contact-left">
      <div>48 rue des Lilas 75011 Paris</div>
      <div>www.orluq-research.example</div>
    </div>

    <div class="contact-right">
      <div class="contact-line">
        <span>555019283</span>
        <svg class="contact-icon" viewBox="0 0 24 24" aria-hidden="true">
          <path d="M6.6 10.8a15.1 15.1 0 0 0 6.6 6.6l2.2-2.2a1 1 0 0 1 1-.25 11.4 11.4 0 0 0 3.6.57 1 1 0 0 1 1 1V20a1 1 0 0 1-1 1A17 17 0 0 1 3 4a1 1 0 0 1 1-1h3.5a1 1 0 0 1 1 1c0 1.25.2 2.45.57 3.57a1 1 0 0 1-.25 1z"/>
        </svg>
      </div>
      <div class="contact-line">
        <span>info@orluq-research.example</span>
        <svg class="contact-icon" viewBox="0 0 24 24" aria-hidden="true">
          <path d="M2 5h20v14H2z" fill="var(--accent-red)"/>
          <path d="M2 5l10 8 10-8" fill="none" stroke="var(--card-surface)" stroke-width="1.6"/>
        </svg>
      </div>
    </div>

    <div class="band-dark"></div>
    <div class="band-red"></div>
  </div>
</body>
</html>
```